Local Chiropractor Needs Up Scale Webdesign

This website needs to have an upscale look with a very modern feel. Below is the information and websites to reference

Add Logo that is attached

Build a color scheme similar to this website image titled "chiro-1"

Must Include these pages in a horizontal menu bar in this order:
Home, Meet Our Staff, Patient Testimonials, Videos, Work Place Wellness, Contact

Build a "classy looking" Make An Appointment Button into the header with the contact info below

Phone Number:
555-314-2706

Address:
4318 Willow Barn Lane, #215
Fernhollow, NV 55492

This website needs 4 rotating banners. Please reference a layout similar to this for the banners: http://drkelmora.com/. However design it nicer than this website, this website is very boring and doesn't flow with the colors properly

Below are the description for each banner

Rotating Banner #1
Use Image: Pediatrics
Two lines of text. First line title line, second description. Use Latin text for fill

Rotating Banner #2
Use Image: Aging Gracefully

Rotating Banner #3
Use Image: Pregnancy

Rotating Banner #4
Use Image: Athletics

I'd like to see a free consultation box similar to the "chiro-1" image. Fields to include are: First Name, Last Name, Phone Number, Comments.

For the body, please fill it with latin text. Please design a professional body layout. You can include a box in the right column for the hours

Office Hours
Monday: 8:00-11:00, 2:00-5:00
Tuesday: 8:30-11:00, 2:00-5:30
Wednesday: 8:00-11:00, 2:00-5:00
Thursday: 10:00-12:00, 2:30-5:00
Friday: 8:00-10:00, 1:00-5:00
Saturday: Closed
Sunday: Closed

For the footer please design something similar to the: http://drkelmora.com/

Also include in the Footer: Powered by Tandem Pixel Works

```html
<!DOCTYPE html>
<html lang="en">
<head>
<meta charset="utf-8">
<title>Evergreen Vitality Chiropractic Health Center</title>
<link rel="stylesheet" href="https://fonts.googleapis.com/css2?family=Mulish:wght@400;600&family=Cormorant+Garamond:ital,wght@0,500;1,500&display=swap">
<style>
:root{
  --dark:#222222;
  --black:#0b0b0b;
  --white:#ffffff;
  --lime:#8dc63f;
  --nav-active:#c5d23a;
  --gold:#c8861a;
  --gold-line:#8a6a1e;
  --green:#2f6b2a;
  --frame:#3f7a3a;
  --text:#1e1e1e;
  --muted:#d8d8d8;
}
*{margin:0;padding:0;box-sizing:border-box}
html,body{width:694px;height:1200px;overflow:hidden;background:var(--white)}
body{font-family:"Mulish",sans-serif;color:var(--text);position:relative}
.abs{position:absolute}

/* header */
.site-header{position:absolute;left:0;top:0;width:694px;height:66px;background:var(--dark)}
.brand{left:16px;top:10px;display:flex;align-items:center;gap:8px;color:var(--lime);font-weight:600}
.brand-dot{width:34px;height:34px;border-radius:50%;background:var(--lime)}
.brand-name{font-size:16px;line-height:17px}
.brand-name small{display:block;font-size:10px;line-height:12px}
.header-address{left:215px;top:32px;color:var(--white);font-size:10px;line-height:15px;letter-spacing:.3px}
.header-phone{left:376px;top:31px;color:var(--white);font-size:8px;letter-spacing:.4px;white-space:nowrap}
.header-phone strong{font-size:12px;font-weight:400;margin-left:3px;letter-spacing:.3px}
.cta-rule{top:18px;width:2px;height:32px;background:var(--white)}
.cta{left:542px;top:21px;width:120px;height:26px;background:var(--gold);color:var(--white);font-size:9px;font-weight:600;letter-spacing:.6px;display:flex;align-items:center;justify-content:center}

/* nav */
.main-nav{left:0;top:68px;width:694px;height:48px;background:var(--black);border-bottom:2px solid var(--gold-line)}
.main-nav ul{list-style:none;display:flex;height:100%;align-items:center;padding-left:29px}
.main-nav li{color:var(--white);font-size:10px;letter-spacing:.8px;padding:0 8px;border-right:1px solid var(--muted);line-height:14px;margin-right:10px}
.main-nav li:first-child{border-left:1px solid var(--muted)}
.main-nav li.active{color:var(--nav-active)}

/* hero */
.hero{left:0;top:118px;width:694px;height:432px;background:linear-gradient(100deg,#dfe9d2 0%,#9fbf6e 30%,#f1e6dc 55%,#e7c9b4 80%,#c9d7a8 100%);border-bottom:3px solid #e4e4e4}
.consult-tab{left:0;top:118px}
.consult-title{left:36px;top:138px;color:var(--white);font-size:15px;letter-spacing:.3px}
.slide-arrow{top:350px}
.slide-title{left:295px;top:411px;width:329px;height:50px;background:rgba(255,255,255,.75);color:var(--green);font-family:"Cormorant Garamond",serif;font-size:37px;letter-spacing:2px;display:flex;align-items:center;justify-content:center}
.slide-text{left:30px;top:468px;width:634px;height:54px;background:rgba(255,255,255,.75);color:var(--green);font-family:"Cormorant Garamond",serif;font-style:italic;font-size:21px;display:flex;align-items:center;padding-left:10px}

/* body */
.intro-title{left:58px;top:593px;font-size:20px;font-weight:400}
.intro-text{left:40px;top:641px;width:318px;font-size:14px;line-height:19.5px;text-align:justify;letter-spacing:.55px}
.hours-box{left:426px;top:577px;width:248px;height:356px;border:2px solid var(--frame);padding:4px}
.hours-inner{width:100%;height:100%;border:1px solid var(--frame);padding:24px 0 0 18px}
.hours-inner h3{font-weight:400;font-size:16px;margin-bottom:18px}
.hours-inner p{font-size:12.5px;height:39px;white-space:nowrap}
.hours-inner b{font-weight:600}

/* footer */
.site-footer{left:0;top:962px;width:694px;height:238px;background:var(--dark);color:var(--white)}
.foot-head{top:30px;font-size:12px;letter-spacing:1.2px;padding-bottom:3px;border-bottom:1px solid #888}
.foot-contact{left:26px;top:62px;font-size:10px;letter-spacing:.5px;line-height:18px}
.foot-contact .num{font-size:14px;letter-spacing:.8px;margin-left:4px}
.foot-contact .addr{font-size:12px;line-height:18px;letter-spacing:.5px}
.map{left:282px;top:32px;width:139px;height:139px;background:linear-gradient(135deg,#e9e3cf,#d6d7c4 50%,#bfd0c9)}
.foot-hours{left:489px;top:62px;font-size:10px;letter-spacing:.6px;line-height:19.2px;white-space:nowrap}
.foot-rule{left:0;top:204px;width:694px;height:1px;background:#444}
.powered{left:24px;top:214px;font-size:8px;color:#bbb;letter-spacing:.4px}
</style>
</head>
<body>

<header class="site-header">
  <div class="abs brand"><span class="brand-dot"></span><span class="brand-name">Evergreen Vitality<small>Chiropractic Health Center</small></span></div>
  <div class="abs header-address">4318 Willow Barn Lane, #215<br>Fernhollow, NV 55492</div>
  <div class="abs header-phone">Phone number: <strong>555-314-2706</strong></div>
  <span class="abs cta-rule" style="left:535px"></span>
  <a class="abs cta">MAKE AN APOINTMENT</a>
  <span class="abs cta-rule" style="left:669px"></span>
</header>

<nav class="abs main-nav">
  <ul>
    <li class="active">HOME</li>
    <li>MEET OUR STAFF</li>
    <li>PATIENT TESTEMONIALS</li>
    <li>VIDEOS</li>
    <li>WORK PLACE WELLNESS</li>
    <li>CONTACT</li>
  </ul>
</nav>

<section class="abs hero" role="img" aria-label="Photo of a smiling mother holding her toddler outdoors on a sunny green lawn"></section>

<svg class="abs consult-tab" width="226" height="98" viewBox="0 0 226 98">
  <polygon points="0,0 225,0 225,44 118,97 0,44" fill="#2b2b2b" fill-opacity=".92"/>
  <polygon points="4,4 221,4 221,41 118,92 4,41" fill="none" stroke="#3f7a3a" stroke-width="1"/>
</svg>
<div class="abs consult-title">CONSULTATION BOX</div>

<svg class="abs slide-arrow" style="left:6px" width="24" height="56" viewBox="0 0 24 56"><polyline points="20,2 4,28 20,54" fill="none" stroke="#555" stroke-width="3"/></svg>
<svg class="abs slide-arrow" style="left:664px" width="24" height="56" viewBox="0 0 24 56"><polyline points="4,2 20,28 4,54" fill="none" stroke="#555" stroke-width="3"/></svg>

<div class="abs slide-title">— PEDIATRICS —</div>
<div class="abs slide-text">”Lorem ipsum dolor sit amet, consectetur adipiscing elit sed do ...”</div>

<main>
  <h1 class="abs intro-title">Lorem ipsum dolor sit amet</h1>
  <p class="abs intro-text">Lorem ipsum dolor sit amet, consectetur adipiscing elit. Integer nec odio. Praesent libero. Sed cursus ante dapibus diam. Sed nisi. Nulla quis sem at nibh elementum imperdiet. Duis sagittis ipsum. Praesent mauris. Fusce nec tellus sed augue semper porta. Mauris massa. Vestibulum lacinia arcu eget nulla. Class aptent taciti sociosqu ad litora torquent per conubia nostra, per inceptos himenaeos. Curabitur sodales porttitor. Morbi lectus risus, iaculis vel, suscipit quis, luctus non, massa. Fusce ac turpis quis ullamcorper.</p>

  <aside class="abs hours-box">
    <div class="hours-inner">
      <h3>Office Hours</h3>
      <p><b>Monday:</b> 8:00-11:00, 2:00-5:00</p>
      <p><b>Tuesday:</b> 8:30-11:00, 2:00-5:30</p>
      <p><b>Wednesday:</b> 8:00-11:00, 2:00-5:00</p>
      <p><b>Thursday:</b> 10:00-12:00, 2:30-5:00</p>
      <p><b>Friday:</b> 8:00-10:00, 1:00-5:00</p>
      <p><b>Saturday:</b> Closed</p>
      <p><b>Sunday:</b> Closed</p>
    </div>
  </aside>
</main>

<footer class="abs site-footer">
  <div class="abs foot-head" style="left:26px">CONTACT</div>
  <div class="abs foot-contact">
    Phone number: <span class="num">555-314-2706</span><br>
    Adress:<br>
    <span class="addr">4318 Willow Barn Lane, #215<br>Fernhollow, NV 55492</span>
  </div>
  <div class="abs map" role="img" aria-label="Street map showing the clinic location"></div>
  <div class="abs foot-head" style="left:489px">OFFICE HOURS</div>
  <div class="abs foot-hours">
    Monday: 8:00-11:00, 2:00-5:00<br>
    Tuesday: 8:30-11:00, 2:00-5:30<br>
    Wednesday: 8:00-11:00, 2:00-5:00<br>
    Thursday: 10:00-12:00, 2:30-5:00<br>
    Friday: 8:00-10:00, 1:00-5:00<br>
    Saturday: Closed<br>
    Sunday: Closed
  </div>
  <div class="abs foot-rule"></div>
  <div class="abs powered">Powered by Tandem Pixel Works</div>
</footer>

</body>
</html>
```